Criação de Projeto Combo top of mind para Tecnologia & Ciencias
" Fazemos assessoria e terceirização de departamento financeiro e temos uma aplicação Web para controle do Depto Financeiro. Resultado do nosso trabalho são relatórios de fluxo de caixa, DRE, balancetes, conta a pagar e receber, integração com escritório de contabilidade e fechamento de custeio e de navios que são demandas especificas do nosso publico alvo "

```html
<!DOCTYPE html>
<html lang="pt-BR">
<head>
<meta charset="utf-8">
<title>Aurevia – Papel Timbrado</title>
<link rel="stylesheet" href="https://fonts.googleapis.com/css2?family=Montserrat:wght@400;500;600;700&display=swap">
<style>
  :root {
    --bg: #e4e5e7;
    --paper: #ffffff;
    --blue: #1d4f8c;
    --green: #7cb342;
    --ink: #2b2b2b;
    --muted: #555b63;
    --faint: #f1f3f2;
  }
  * { box-sizing: border-box; margin: 0; padding: 0; }
  html, body { width: 1200px; height: 1200px; overflow: hidden; }
  body {
    background: var(--bg);
    font-family: "Montserrat", sans-serif;
    color: var(--ink);
  }
  .letterhead {
    position: absolute;
    left: 220px; top: 62px;
    width: 760px; height: 1075px;
    background: var(--paper);
    overflow: hidden;
  }
  .brand {
    position: absolute; left: 80px; top: 60px;
    display: flex; align-items: center; gap: 12px;
  }
  .brand-dot {
    width: 34px; height: 34px; border-radius: 50%;
    background: var(--green);
  }
  .brand-name {
    font-weight: 700; font-size: 26px; letter-spacing: 1px;
    color: var(--blue); line-height: 1;
  }
  .brand-line {
    font-weight: 500; font-size: 10px;
    color: var(--muted); margin-top: 5px;
  }
  .header-rule {
    position: absolute; left: 0; top: 147px;
    width: 700px; height: 2px; background: var(--green);
  }
  .emblem {
    position: absolute; left: 230px; top: 400px;
    width: 300px; height: 300px; border-radius: 50%;
    background: var(--faint);
  }
  .recipient {
    position: absolute; left: 80px; top: 300px;
    font-size: 8.5px; line-height: 1.55; color: var(--muted);
  }
  .recipient .to { font-weight: 700; color: var(--ink); font-size: 10px; }
  .recipient .name { font-weight: 700; color: var(--ink); font-size: 10px; }
  .body-copy {
    position: absolute; left: 80px; top: 428px; width: 600px;
    font-size: 8.5px; line-height: 1.5; color: var(--muted);
  }
  .body-copy p { margin-bottom: 10px; }
  .signature {
    position: absolute; left: 80px; top: 780px;
    width: 150px; height: 42px; background: var(--faint);
  }
  .signer {
    position: absolute; left: 80px; top: 848px;
    font-size: 9.5px; line-height: 1.45;
  }
  .signer .name { font-weight: 700; }
  .signer .role { font-size: 8px; color: var(--muted); }
  .footer-rule {
    position: absolute; left: 80px; top: 975px; width: 600px; height: 3px;
    display: flex;
  }
  .footer-rule .blue { flex: 0 0 48%; background: var(--blue); }
  .footer-rule .green { flex: 1; background: var(--green); }
  .contacts {
    position: absolute; left: 80px; top: 995px; width: 600px;
    display: flex; justify-content: space-between;
    font-size: 9px; color: var(--blue); line-height: 1.55; font-weight: 500;
  }
  .contact { display: flex; align-items: flex-start; gap: 8px; }
  .contact svg { flex: 0 0 auto; margin-top: 1px; }
</style>
</head>
<body>
  <main class="letterhead">
    <header class="brand">
      <span class="brand-dot"></span>
      <div>
        <div class="brand-name">AUREVIA</div>
        <div class="brand-line">Finanças &amp; Sistemas</div>
      </div>
    </header>
    <div class="header-rule"></div>

    <div class="emblem"></div>

    <section class="recipient">
      <div class="to">TO</div>
      <div class="name">Lucas Ferreira</div>
      <div>Human Resources</div>
      <div>Nortelis Ltda.</div>
      <div>1100 Rua Aurora, Centro</div>
      <div>SP 01234</div>
    </section>

    <section class="body-copy">
      <p>Lorem ipsum dolor sit amet, consectetuer adipiscing elit, sed diam nonummy nibh euismod tincidunt ut laoreet dolore magna aliquam erat volutpat. Ut wisi enim ad minim veniam, quis nostrud exerci tation ullamcorper suscipit lobortis nisl ut aliquip ex ea commodo consequat. Duis autem vel eum iriure dolor in hendrerit in vulputate velit esse molestie consequat, vel illum dolore eu feugiat nulla facilisis at vero eros et accumsan et iusto odio dignissim qui blandit praesent luptatum zzril delenit augue duis dolore te feugait nulla facilisi.</p>
      <p>Nam liber tempor cum soluta nobis eleifend option congue nihil imperdiet doming id quod mazim placerat facer possim assum. Typi non habent claritatem insitam.</p>
      <p>Est usus legentis in iis qui facit eorum claritatem.</p>
      <p>Investigationes demonstraverunt lectores legere me lius quod ii legunt saepius. Claritas est etiam processus dynamicus, qui sequitur mutationem consuetudium lectorum. Mirum est notare quam littera gothica, quam nunc putamus parum claram, anteposuerit litterarum formas humanitatis per seacula quarta decima et quinta decima. Eodem modo typi, qui nunc nobis videntur parum clari, fiant sollemnes in futurum.</p>
      <p>Consectetuer adipiscing elit, sed diam nonummy nibh euismod tincidunt ut laoreet dolore magna aliquam erat volutpat. Ut wisi enim ad minim veniam, quis nostrud exerci tation ullamcorper suscipit lobortis nisl ut aliquip ex ea commodo consequat. Duis autem vel eum iriure dolor in hendrerit in vulputate velit esse molestie consequat, vel illum dolore eu feugiat nulla facilisis at vero eros et accumsan et iusto odio dignissim qui blandit praesent luptatum zzril delenit augue duis dolore te feugait nulla facilisi.</p>
      <p>Nam liber tempor cum soluta nobis eleifend option congue nihil imperdiet.</p>
    </section>

    <div class="signature" role="img" aria-label="Handwritten signature of Rafael Duarte"></div>
    <div class="signer">
      <div class="name">Rafael Duarte</div>
      <div class="role">Managing Director</div>
    </div>

    <div class="footer-rule"><span class="blue"></span><span class="green"></span></div>

    <footer class="contacts">
      <div class="contact">
        <svg width="16" height="16" viewBox="0 0 16 16" aria-hidden="true">
          <circle cx="8" cy="8" r="8" fill="var(--blue)"/>
          <path d="M5.2 4.2l1.4-.3.8 1.9-.9.7c.5 1.1 1.3 1.9 2.4 2.4l.7-.9 1.9.8-.3 1.4c-3.3.3-6.3-2.7-6-6z" fill="#fff"/>
        </svg>
        <div>+55 (11) 4000-1234<br>+55 (11) 4000-5678</div>
      </div>
      <div class="contact">
        <svg width="16" height="16" viewBox="0 0 16 16" aria-hidden="true">
          <circle cx="8" cy="8" r="8" fill="var(--blue)"/>
          <rect x="4" y="5.2" width="8" height="5.6" rx="0.6" fill="none" stroke="#fff" stroke-width="1"/>
          <path d="M4.2 5.6L8 8.4l3.8-2.8" fill="none" stroke="#fff" stroke-width="1"/>
        </svg>
        <div>contato@aurevia.com.br<br>www.aurevia.com.br</div>
      </div>
      <div class="contact">
        <svg width="16" height="16" viewBox="0 0 16 16" aria-hidden="true">
          <circle cx="8" cy="8" r="8" fill="var(--blue)"/>
          <path d="M8 3.6a2.9 2.9 0 0 0-2.9 2.9C5.1 8.7 8 12.4 8 12.4s2.9-3.7 2.9-5.9A2.9 2.9 0 0 0 8 3.6z" fill="#fff"/>
          <circle cx="8" cy="6.5" r="1.1" fill="var(--blue)"/>
        </svg>
        <div>Rua das Palmeiras, 250<br>Bairro Jardim Azul<br>01234-000 - São Paulo / SP</div>
      </div>
    </footer>
  </main>
</body>
</html>
```